Facebook ads needed for Pharmacy Continuing Education

I need 5 different Facebook ads in 3 sizes:

1080X1080, ratio 1:1
1080x1920
1200x628

I need the created ads in .psd format. Please ensure that all fonts used in the PSD file are standard system fonts or commonly available fonts in Adobe Photoshop (e.g., from the Adobe Fonts library). Do not use paid or third-party fonts that are not included with Photoshop by default.

Please check out the Vomedo.com homepage to get an idea of the look and feel of the images we want. I have also uploaded some past ads we like
and our logo.

Text:

Free California Cultural Competency CE for Pharmacy Techs

BKTL Approved
Easy-To-Use
Dalvix Ledger Submission

Button: Get Your Free Course

```html
<!DOCTYPE html>
<html lang="en">
<head>
<meta charset="utf-8">
<title>Vomedo – Free California Cultural Competency CE ads</title>
<link rel="stylesheet" href="https://fonts.googleapis.com/css2?family=Bebas+Neue&family=Questrial&display=swap">
<style>
  :root {
    --board-green: #5a8414;
    --navy: #053a63;
    --ink: #0a3a66;
    --leaf: #6ba315;
    --logo-green: #5fa327;
    --orange: #e08e3f;
    --white: #ffffff;
    --scrub-blue: #1a7ff0;
    --coat: #c3d6f3;
  }
  * { box-sizing: border-box; margin: 0; padding: 0; }
  html, body { width: 1200px; height: 1200px; overflow: hidden; }
  body { background: var(--board-green); position: relative; font-family: "Questrial", sans-serif; }

  .ad {
    position: absolute; width: 480px; height: 480px; overflow: hidden;
    box-shadow: 6px 10px 22px rgba(0,0,0,0.35);
  }
  .ad--one { left: 96px; top: 82px; background: var(--white); }
  .ad--two { left: 624px; top: 82px; background: var(--navy); }
  .ad--three { left: 96px; top: 638px; background: var(--navy); }
  .ad--four { left: 624px; top: 638px; background: var(--white); }

  .shape { position: absolute; left: 0; top: 0; }

  .brand {
    position: absolute; display: flex; align-items: center; gap: 6px;
    font-family: "Questrial", sans-serif; font-size: 50px; line-height: 1; color: var(--ink);
  }
  .brand__dot { width: 34px; height: 34px; border-radius: 50%; background: var(--logo-green); flex: none; }
  .brand--light { color: var(--white); }
  .brand--light .brand__dot { background: var(--white); }

  .headline {
    position: absolute; font-family: "Bebas Neue", sans-serif; font-size: 29px;
    line-height: 32px; letter-spacing: 0.2px; color: var(--ink);
  }
  .headline--light { color: var(--white); }

  .free-tag {
    position: absolute; background: var(--orange); color: var(--white);
    font-family: "Bebas Neue", sans-serif; font-size: 54px; line-height: 50px;
    padding: 3px 14px 0; transform: rotate(-2deg);
  }

  .benefits { position: absolute; list-style: none; color: var(--ink); font-size: 22px; line-height: 28px; }
  .benefits--light { color: var(--white); }
  .benefits li { position: relative; padding-left: 28px; }
  .benefits svg { position: absolute; left: 0; top: 6px; width: 21px; height: 21px; }
  .benefits--large { font-size: 25px; line-height: 31px; }
  .benefits--large li { padding-left: 30px; }
  .benefits--large svg { top: 7px; width: 23px; height: 23px; }

  .cta {
    position: absolute; height: 39px; padding: 0 13px; border-radius: 20px;
    background: var(--orange); color: var(--white);
    font-family: "Bebas Neue", sans-serif; font-size: 17px; letter-spacing: 0.4px;
    display: flex; align-items: center; justify-content: center;
  }

  .artwork { position: absolute; }
</style>
</head>
<body>

<svg width="0" height="0" style="position:absolute">
  <defs>
    <symbol id="tick" viewBox="0 0 24 24">
      <circle cx="11" cy="13" r="9" fill="none" stroke="currentColor" stroke-width="1.8"/>
      <path d="M6.5 12.5 L10.5 16.5 L22 3" fill="none" stroke="currentColor" stroke-width="2.2" stroke-linecap="round" stroke-linejoin="round"/>
    </symbol>
  </defs>
</svg>

<!-- Ad 1: white, duo of staff -->
<section class="ad ad--one">
  <svg class="shape" width="480" height="480" viewBox="0 0 480 480">
    <circle cx="380" cy="400" r="176" fill="var(--navy)"/>
  </svg>
  <div class="artwork" role="img" aria-label="Illustration of a pharmacy tech in blue scrubs and a pharmacist in a white coat"
       style="left:242px; top:28px; width:238px; height:452px; background:linear-gradient(90deg, var(--scrub-blue) 0%, var(--scrub-blue) 45%, var(--coat) 55%, #2a3340 100%); opacity:0.9;"></div>
  <div class="brand" style="left:11px; top:28px;"><span>Vomedo</span><span class="brand__dot"></span></div>
  <h2 class="headline" style="left:11px; top:146px;">Free California<br>Cultural Competency<br>CE for Pharmacy Techs</h2>
  <ul class="benefits" style="left:12px; top:246px;">
    <li><svg><use href="#tick"/></svg>BKTL Approved</li>
    <li><svg><use href="#tick"/></svg>Easy-To-Use</li>
    <li><svg><use href="#tick"/></svg>Dalvix Ledger<br>Submission</li>
  </ul>
  <div class="cta" style="left:12px; top:408px; width:161px;">Get Your Free Course</div>
</section>

<!-- Ad 2: navy with green diagonal -->
<section class="ad ad--two">
  <svg class="shape" width="480" height="480" viewBox="0 0 480 480">
    <polygon points="452,0 480,0 480,480 177,480" fill="var(--leaf)"/>
  </svg>
  <div class="artwork" role="img" aria-label="Illustration of a pharmacist in a light blue lab coat"
       style="left:258px; top:22px; width:196px; height:458px; background:linear-gradient(180deg, #1e2a33 0%, #1e2a33 25%, var(--coat) 26%, var(--coat) 94%, var(--scrub-blue) 95%);"></div>
  <div class="brand brand--light" style="left:11px; top:28px;"><span>Vomedo</span><span class="brand__dot"></span></div>
  <div class="free-tag" style="left:13px; top:122px;">Free</div>
  <h2 class="headline headline--light" style="left:11px; top:180px;">California Cultural<br>Competency CE for<br>Pharmacy Techs</h2>
  <ul class="benefits benefits--light" style="left:12px; top:275px;">
    <li><svg><use href="#tick"/></svg>BKTL Approved</li>
    <li><svg><use href="#tick"/></svg>Easy-To-Use</li>
    <li><svg><use href="#tick"/></svg>Dalvix Ledger<br>Submission</li>
  </ul>
  <div class="cta" style="left:12px; top:408px; width:161px;">Get Your Free Course</div>
</section>

<!-- Ad 3: navy with lab scene -->
<section class="ad ad--three">
  <div class="free-tag" style="left:12px; top:12px;">Free</div>
  <h2 class="headline headline--light" style="left:11px; top:70px;">California Cultural<br>Competency CE for<br>Pharmacy Techs</h2>
  <ul class="benefits benefits--light benefits--large" style="left:263px; top:42px;">
    <li><svg><use href="#tick"/></svg>BKTL Approved</li>
    <li><svg><use href="#tick"/></svg>Easy-To-Use</li>
    <li><svg><use href="#tick"/></svg>Dalvix Ledger<br>Submission</li>
  </ul>
  <div class="brand brand--light" style="left:88px; top:196px; font-size:30px; gap:4px;"><span>Vomedo</span><span class="brand__dot" style="width:20px;height:20px;"></span></div>
  <div class="cta" style="left:225px; top:193px; width:161px;">Get Your Free Course</div>
  <div class="artwork" role="img" aria-label="Illustration of a laboratory with three staff, shelves of glassware and charts on the wall"
       style="left:22px; top:253px; width:434px; height:227px; background:linear-gradient(180deg, #5d6fbf 0%, #e9eef8 55%, #6a78c8 100%); opacity:0.85;"></div>
</section>

<!-- Ad 4: white with navy band -->
<section class="ad ad--four">
  <svg class="shape" width="480" height="480" viewBox="0 0 480 480">
    <polygon points="0,204 480,163 480,340 0,390" fill="var(--navy)"/>
  </svg>
  <div class="artwork" role="img" aria-label="Illustration of a pharmacist with goggles holding a tablet"
       style="left:222px; top:120px; width:258px; height:360px; background:linear-gradient(160deg, #1c2450 0%, #f28a8a 28%, #f4f6fa 50%, #dbe7f5 100%);"></div>
  <div class="brand" style="left:11px; top:62px;"><span>Vomedo</span><span class="brand__dot"></span></div>
  <h2 class="headline" style="left:227px; top:24px;">Free California<br>Cultural Competency<br>CE for Pharmacy Techs</h2>
  <ul class="benefits benefits--light" style="left:12px; top:236px;">
    <li><svg><use href="#tick"/></svg>BKTL Approved</li>
    <li><svg><use href="#tick"/></svg>Easy-To-Use</li>
    <li><svg><use href="#tick"/></svg>Dalvix Ledger<br>Submission</li>
  </ul>
  <div class="cta" style="left:12px; top:408px; width:161px;">Get Your Free Course</div>
</section>

</body>
</html>
```